Events and Parties web-site needs a Web Design

VoTrel needs a web design.
VoTrel means The Bees in Italian.
VoTrel target market is people who is organizing parties and events.
Our mission is that the parties and events of our clients exceed their expectations by providing them web and mobile tools.
Our vision is to be the best and biggest party web portal of the country.
The main features of our web site is to let people invite guests and search suppliers/providers. Guests will also confirm presence (RSVP) and buy presents/gifts at the site as well.
Our slogan is "Curta sua festa desde já !" that means "Enjoy our party now !" in Brazilian Portuguese.
The idea here is that the party starts now and not only at the scheduled date and time.
Updates
It seems that must have and nice to have briefing is not appearing to you as I filled. So I will type it agai here:
Our slogan text that is "Curta sua festa desde já !" that means "Enjoy your party now !".
Space to paid ads.
Language switch to Spanish. Brazilian Portuguese is our default language.
Logon form with 2 inputs: Email and password.
RSVP form with 2 inputs: Event ID and password
Kendro trusted site seal (SSL/HTTPS) logo.
Update to my briefing: Only event organizer and guests will be able to see details of the events/parties like photos/blog, guest list and etc. Suppliers will be searched and rated like stayvoro.com/roamgliq.
Target Market(s)
VoTrel target market is amateur and professional people who are organizing parties and events.
Our mission is that the parties and events of our clients exceed their expectations by providing them easy and fast web and mobile tools.
Our vision is to be the best and biggest party portal of our country.
The main features of our web site is to let people invite guests and search suppliers/providers. Guests will also confirm presence (RSVP) and buy presents at the site.
Industry/Entity Type
Events
Requirements
Must have
- Design and colors compliant with attached logo.
- Our slogan text that is "Curta sua festa desde já !" that means "Enjoy your party now !".
- Space to paid ads.
- Language switch to Spanish. Brazilian Portuguese is our default language.
- Logon form with 2 inputs: Email and password.
- RSVP form with 2 inputs: Event ID and password
- Kendro trusted site seal (SSL/HTTPS) logo.
Nice to have
- VoTrel stands for The Bees in Italian. It would be very nice to have a not so explicit idea that each user is a bee and VoTrel is the hive where party/event occurs.
Should not have
- No PageMill please.
- No infant/child oriented designs please. Our market is not only children birthdays but also other parties and events like marriages, corporate events and so on

```html
<!DOCTYPE html>
<html lang="pt-BR">
<head>
<meta charset="utf-8">
<title>VoTrel – Curta sua festa desde já</title>
<link href="https://fonts.googleapis.com/css2?family=Jost:wght@400;500&family=Arimo:wght@400;700&family=Pacifico&display=swap" rel="stylesheet">
<style>
:root{
  --orange:#f6a21a;
  --orange-deep:#ef5b0c;
  --brown:#2c0907;
  --brown-mid:#3d1411;
  --footer:#4a2a26;
  --ink:#3a2c28;
  --muted:#8a7f7b;
  --line:#dcdcdc;
  --paper:#f4f4f4;
  --white:#ffffff;
}
*{box-sizing:border-box;margin:0;padding:0}
html,body{width:692px;height:1200px;overflow:hidden;background:var(--white)}
body{position:relative;font-family:"Arimo",Arial,sans-serif;color:var(--ink)}
.abs{position:absolute}

/* header */
.site-header{left:0;top:0;width:692px;height:70px;background:linear-gradient(#fff,#efefef);border-bottom:1px solid #e2e2e2}
.brand{left:60px;top:12px;width:46px;text-align:center}
.brand-mark{width:28px;height:28px;border-radius:50%;background:var(--orange);margin:0 auto 3px}
.brand-name{font-family:"Jost",sans-serif;font-size:16px;color:var(--orange);line-height:1}
.tagline{right:60px;top:15px;font-family:"Jost",sans-serif;font-size:14px;color:var(--ink)}
.tagline span{color:var(--orange)}
.main-nav{left:244px;top:38px;display:flex;gap:6px;font-family:"Jost",sans-serif;font-size:11px;color:var(--ink)}
.main-nav a{color:inherit;text-decoration:none}
.main-nav .sep{color:#aaa}
.main-nav .active{color:var(--orange);border-bottom:1px solid var(--orange)}
.search{left:523px;top:39px;width:109px;height:16px;border-bottom:1px solid #888;font-size:9px;color:#777;padding-left:2px}
.search svg{position:absolute;right:2px;top:2px}

/* hero */
.hero-bg{left:0;top:70px;width:692px;height:280px;background:radial-gradient(ellipse at 55% 30%,#6a5a44 0%,#2a2520 55%,#121416 100%)}
.hero-wave{left:0;top:310px;width:692px;height:60px}
.slogan{left:60px;top:90px;font-family:"Jost",sans-serif;font-style:italic;font-size:15px;color:var(--white)}
.hero-tabs{left:352px;top:70px;display:flex;gap:7px}
.tab{width:65px;height:44px;background:linear-gradient(#fff,#e6e6e6);font-size:7px;color:#666;text-align:center;padding-top:8px}
.tab.active{background:var(--orange);color:var(--white)}
.tab i{display:block;width:12px;height:12px;margin:0 auto 4px;border-radius:2px;background:#888}
.tab.active i{background:#fff;border-radius:50%}
.slider{left:78px;top:128px;width:536px;height:289px;background:radial-gradient(ellipse at 55% 35%,#8a7560 0%,#3a2e26 50%,#0e0c0b 100%)}
.slider-caption{left:78px;top:321px;width:536px;height:96px;background:rgba(0,0,0,.55);text-align:center;color:var(--white)}
.slider-title{font-family:"Pacifico",cursive;font-size:24px;margin-top:4px;line-height:1.3}
.slider-text{font-size:9px}
.btn-more{display:inline-block;margin-top:9px;width:97px;height:25px;background:linear-gradient(#fb9a25,#ee5f0d);border-radius:3px;font-family:"Pacifico",cursive;font-size:12px;line-height:25px}
.slider-arrow{top:253px;width:23px;height:23px;border-radius:50%;background:rgba(220,220,220,.85)}
.slider-arrow svg{display:block;margin:6px auto}

/* signup */
.signup{left:60px;top:454px;width:379px;height:166px;background:var(--paper);padding:5px}
.signup-title{height:34px;text-align:center;font-family:"Jost",sans-serif;font-size:14px;line-height:34px;color:var(--ink)}
.signup-body{background:var(--white);height:123px;text-align:center;padding-top:11px;font-size:9px;color:#555}
.signup-body b{color:var(--orange-deep)}
.field{height:24px;border:1px solid #ccc;font-size:8px;color:#888;text-align:left;padding:0 7px;line-height:22px;background:#fff}
.signup-fields{display:flex;gap:11px;margin:11px 0 0 62px}
.signup-fields .field{width:122px}
.btn-create{margin:11px 0 0 62px;width:253px;height:22px;background:linear-gradient(#fb7a20,#e5460a);color:#fff;font-weight:700;font-size:9px;line-height:22px}
.terms{margin-top:6px;font-size:8px;color:var(--muted)}

/* calendar */
.calendar{left:458px;top:454px;width:174px;height:167px;background:#ececec;border:1px solid #ccc}
.cal-head{height:26px;background:#1c1c1c;color:#fff;font-family:"Jost",sans-serif;font-size:11px;text-align:center;line-height:26px;position:relative}
.cal-head .prev{position:absolute;left:8px}.cal-head .next{position:absolute;right:8px}
.cal-grid{display:grid;grid-template-columns:repeat(7,1fr);padding:4px 6px;row-gap:6px;font-size:6.5px;text-align:center;color:#bbb}
.cal-grid .dow{color:#e0602a;font-size:7px}
.cal-grid .today{color:#333}

/* venues */
.section-title{left:0;top:648px;width:692px;text-align:center;font-family:"Jost",sans-serif;font-size:23px;color:var(--ink);letter-spacing:.5px}
.title-rule{left:138px;top:690px;width:416px;height:1px;background:var(--line)}
.title-dot{left:343px;top:687px;width:6px;height:6px;border-radius:50%;background:#ccc}
.venues{left:60px;top:713px;display:flex;gap:8px}
.venue{width:137px;height:143px;background:var(--paper);border:1px solid #e3e3e3}
.venue-photo{height:73px}
.venue h3{font-family:"Jost",sans-serif;font-weight:400;font-size:11px;margin:6px 0 0 8px}
.stars{color:var(--orange);font-size:7px;margin-left:8px;letter-spacing:1px}
.venue p{font-size:7px;line-height:1.35;color:var(--muted);margin:2px 8px 0}
.venue.featured{background:var(--brown-mid);color:#fff}
.venue.featured p{color:#e6d6d2}

/* dark band */
.dark-band{left:0;top:890px;width:692px;height:212px;background:var(--brown)}
.zigzag{left:0;top:884px}
.band-title{font-family:"Jost",sans-serif;font-size:17px;color:#fff;top:914px}
.band-rule{top:940px;height:1px;background:#4a1f1b}
.events-box{left:60px;top:962px;width:278px;height:108px;border:1px solid #4a1c18;background:#33100d}
.phone{left:72px;top:950px;width:80px;height:120px;border-radius:10px;background:#222;border:2px solid #999}
.phone-screen{left:77px;top:970px;width:70px;height:98px;background:linear-gradient(#3a2a20,#ddd 50%,#f4f4f4)}
.events-copy{left:169px;top:975px;width:160px;font-size:7px;line-height:1.25;color:#e8dcd9}
.events-copy h4{font-weight:400;font-size:9px;color:#fff}
.events-copy h5{font-weight:400;font-size:9px;color:var(--orange);margin-top:3px}
.events-copy .hl{color:var(--orange)}
.login-box{left:377px;top:962px;width:255px;height:108px;border:1px solid #4a1c18;background:#33100d}
.login-box .field{position:absolute;left:19px;width:217px;height:21px;background:#2a0a08;border-color:#5a2a24;color:#b89e98;line-height:19px}
.btn-login{left:485px;top:1038px;width:128px;height:21px;background:#2a0a08;border:1px solid #5a2a24;color:#fff;font-size:9px;line-height:19px;padding-left:17px}
.btn-login i{position:absolute;right:0;top:0;width:21px;height:19px;background:var(--orange)}
.btn-login svg{position:absolute;right:6px;top:5px}

/* footer */
.site-footer{left:0;top:1102px;width:692px;height:98px;background:var(--footer);color:#fff}
.footer-head{font-family:"Jost",sans-serif;font-size:12px;color:#fff}
.quick-links{left:61px;top:1135px;font-size:9px;color:#d9c6c2;display:flex;gap:7px;align-items:center}
.quick-links i{width:4px;height:4px;background:var(--orange)}
.footer-brand{left:346px;top:1118px;transform:translateX(-50%);text-align:center}
.footer-brand .brand-mark{width:28px;height:28px;background:#777}
.footer-brand .brand-name{color:#fff;font-size:14px}
.socials{left:520px;top:1136px;display:flex;gap:6px}
.socials i{width:8px;height:8px;border-radius:50%;background:#cdbab6}
.copyright{left:0;top:1169px;width:692px;text-align:center;font-size:7px;color:#cdbab6}
</style>
</head>
<body>

<header class="site-header abs">
  <div class="brand abs"><div class="brand-mark"></div><div class="brand-name">VoTrel</div></div>
  <div class="tagline abs"><span>A Plataforma Digital Para Você</span> Organizar Seu Evento</div>
  <nav class="main-nav abs">
    <a class="active">Contatti</a><span class="sep">·</span><a>Faq</a><span class="sep">·</span><a>Newsletter</a><span class="sep">·</span><a>Friends</a><span class="sep">·</span><a>Pubblicità</a>
  </nav>
  <div class="search abs">Search
    <svg width="9" height="9" viewBox="0 0 10 10"><circle cx="4" cy="4" r="3" fill="none" stroke="#333" stroke-width="1.4"/><line x1="6.2" y1="6.2" x2="9.5" y2="9.5" stroke="#333" stroke-width="1.6"/></svg>
  </div>
</header>

<div class="hero-bg abs" role="img" aria-label="Party scene with dancers and loudspeakers"></div>
<svg class="hero-wave abs" viewBox="0 0 692 60" preserveAspectRatio="none"><path d="M0 17 Q346 70 692 17 L692 60 L0 60Z" fill="#fff"/></svg>
<div class="slogan abs">"Curta sua festa desde já !"</div>
<div class="hero-tabs abs">
  <div class="tab active"><i></i>Crea Event</div>
  <div class="tab"><i></i>Condividi Eventi</div>
  <div class="tab"><i></i>Gestisci Event</div>
  <div class="tab"><i></i>Login Faceloop</div>
</div>
<div class="slider abs" role="img" aria-label="Couple dancing at a party"></div>
<div class="slider-caption abs">
  <div class="slider-title">Welcome to VoTrel</div>
  <div class="slider-text">It is a long established fact that a reader will be distracted by the</div>
  <div class="btn-more">View More</div>
</div>
<div class="slider-arrow abs" style="left:66px"><svg width="8" height="11" viewBox="0 0 8 11"><path d="M6 1 L2 5.5 L6 10" fill="none" stroke="#444" stroke-width="2"/></svg></div>
<div class="slider-arrow abs" style="left:602px"><svg width="8" height="11" viewBox="0 0 8 11"><path d="M2 1 L6 5.5 L2 10" fill="none" stroke="#444" stroke-width="2"/></svg></div>

<section class="signup abs">
  <div class="signup-title">— Start Your Event Now! —</div>
  <div class="signup-body">
    Setting up an Account is Quick, Easy, and <b>FREE</b>.
    <div class="signup-fields"><div class="field">Event ID*</div><div class="field">Email ID*</div></div>
    <div class="btn-create">Create My Account</div>
    <div class="terms">By Creating an Account, You agree to our terms &amp; conditions</div>
  </div>
</section>

<aside class="calendar abs">
  <div class="cal-head"><span class="prev">◀</span>March 2014<span class="next">▶</span></div>
  <div class="cal-grid">
    <span class="dow">Mon</span><span class="dow">Tue</span><span class="dow">Wed</span><span class="dow">Thu</span><span class="dow">Fri</span><span class="dow">Sat</span><span class="dow">Sun</span>
    <span>27</span><span>28</span><span>29</span><span>01</span><span>02</span><span>03</span><span>04</span>
    <span>05</span><span>06</span><span class="today">07</span><span>08</span><span>09</span><span>10</span><span>11</span>
    <span>12</span><span>13</span><span>14</span><span>15</span><span>16</span><span>17</span><span>18</span>
    <span>19</span><span>20</span><span>21</span><span>22</span><span>23</span><span>24</span><span>25</span>
    <span>26</span><span>27</span><span>28</span><span>29</span><span>30</span><span>31</span><span></span>
  </div>
</aside>

<h2 class="section-title abs">POPULAR VENUES IN COLOGNE</h2>
<div class="title-rule abs"></div><div class="title-dot abs"></div>
<div class="venues abs">
  <article class="venue"><div class="venue-photo" style="background:linear-gradient(#c9c9c9,#7a4a22)" role="img" aria-label="Burger on a plate"></div><h3>Der Rote Ochse</h3><div class="stars">★★★★★</div><p>It is a long established fact that a reader will be distracted by the readable content.</p></article>
  <article class="venue featured"><div class="venue-photo" style="background:radial-gradient(#c9a27a,#3e2416)" role="img" aria-label="Latte art in a coffee cup"></div><h3>Cafe Lungo</h3><div class="stars">★★★★★</div><p>It is a long established fact that a reader will be distracted by the readable content.</p></article>
  <article class="venue"><div class="venue-photo" style="background:linear-gradient(#8a5a3a,#c67a4a)" role="img" aria-label="Grilled chicken salad"></div><h3>Marenzo</h3><div class="stars">★★★★★</div><p>It is a long established fact that a reader will be distracted by the readable content.</p></article>
  <article class="venue"><div class="venue-photo" style="background:linear-gradient(#3a3634,#7a6a5c)" role="img" aria-label="Gift box of spices and coffee"></div><h3>Kolmar Finest</h3><div class="stars">★★★★★</div><p>It is a long established fact that a reader will be distracted by the readable content.</p></article>
</div>

<div class="dark-band abs"></div>
<svg class="zigzag abs" width="692" height="8" viewBox="0 0 692 8"><path d="M0 8 L0 4 Q0 4 0 4 L4 0 L8 4 L12 0 L16 4 L20 0 L24 4 L28 0 L32 4 L36 0 L40 4 L44 0 L48 4 L52 0 L56 4 L60 0 L64 4 L68 0 L72 4 L76 0 L80 4 L84 0 L88 4 L92 0 L96 4 L100 0 L104 4 L108 0 L112 4 L116 0 L120 4 L124 0 L128 4 L132 0 L136 4 L140 0 L144 4 L148 0 L152 4 L156 0 L160 4 L164 0 L168 4 L172 0 L176 4 L180 0 L184 4 L188 0 L192 4 L196 0 L200 4 L204 0 L208 4 L212 0 L216 4 L220 0 L224 4 L228 0 L232 4 L236 0 L240 4 L244 0 L248 4 L252 0 L256 4 L260 0 L264 4 L268 0 L272 4 L276 0 L280 4 L284 0 L288 4 L292 0 L296 4 L300 0 L304 4 L308 0 L312 4 L316 0 L320 4 L324 0 L328 4 L332 0 L336 4 L340 0 L344 4 L348 0 L352 4 L356 0 L360 4 L364 0 L368 4 L372 0 L376 4 L380 0 L384 4 L388 0 L392 4 L396 0 L400 4 L404 0 L408 4 L412 0 L416 4 L420 0 L424 4 L428 0 L432 4 L436 0 L440 4 L444 0 L448 4 L452 0 L456 4 L460 0 L464 4 L468 0 L472 4 L476 0 L480 4 L484 0 L488 4 L492 0 L496 4 L500 0 L504 4 L508 0 L512 4 L516 0 L520 4 L524 0 L528 4 L532 0 L536 4 L540 0 L544 4 L548 0 L552 4 L556 0 L560 4 L564 0 L568 4 L572 0 L576 4 L580 0 L584 4 L588 0 L592 4 L596 0 L600 4 L604 0 L608 4 L612 0 L616 4 L620 0 L624 4 L628 0 L632 4 L636 0 L640 4 L644 0 L648 4 L652 0 L656 4 L660 0 L664 4 L668 0 L672 4 L676 0 L680 4 L684 0 L688 4 L692 0 L692 8Z" fill="#2c0907"/></svg>

<h2 class="band-title abs" style="left:60px">Our Events</h2>
<div class="band-rule abs" style="left:60px;width:278px"></div>
<h2 class="band-title abs" style="left:376px">Login Form</h2>
<div class="band-rule abs" style="left:376px;width:256px"></div>

<div class="events-box abs"></div>
<div class="phone abs"></div>
<div class="phone-screen abs" role="img" aria-label="Mobile preview of the site"></div>
<div class="events-copy abs">
  <h4>There are many variations</h4>
  Passages of Lorem Ipsum available, but the majority have suffered alteration in some form, by injected humour, or randomised words which don't look even slightly
  <h5>If you are going to use a passage</h5>
  <span class="hl">Lorem Ipsum, you need to be sure there isn't anything embarrassing hidden in the middle of text. All the Lorem Ipsum generators</span>
</div>

<div class="login-box abs">
  <div class="field" style="top:19px">Email*</div>
  <div class="field" style="top:48px">Password*</div>
</div>
<div class="btn-login abs">Login For Send<i></i><svg width="8" height="9" viewBox="0 0 8 9"><path d="M0 0 L8 4.5 L0 9Z" fill="#fff"/></svg></div>

<footer class="site-footer abs"></footer>
<div class="footer-head abs" style="left:61px;top:1112px">Quick links</div>
<div class="quick-links abs">Contatti<i></i>Faq<i></i>Newsletter<i></i>Friends<i></i>Pubblicità</div>
<div class="footer-brand abs"><div class="brand-mark"></div><div class="brand-name">VoTrel</div></div>
<div class="footer-head abs" style="left:520px;top:1112px">Follow us on</div>
<div class="socials abs" aria-label="Social channels"><i></i><i></i><i></i><i></i><i></i><i></i><i></i><i></i></div>
<div class="copyright abs">© 2014 votrel.com. All Rights Reserved.</div>

</body>
</html>
```